TRAVEX CONSULTING / PROJECT MANAGEMENT WEB DESIGN

Design Brief: Travex Consulting Website

I own 'TRAVEX' business name and therefore can keep the name and logo simple i.e. TRAVEX only and incorporate consulting / Project Management within the design or text.

Purpose:

The purpose of this project is to create a website for Travex.com.au, a project management consulting company. The website will promote the company's services, allowing potential clients to learn more about Travex and its capabilities. The website should be professional, easy to navigate, and provide all necessary information for potential clients.

Target Audience:

Clients in the Oil & Gas, LNG, and Chemical industry
Businesses and organizations in need of project management and engineering consultancy services
Potential clients looking for information about the company and its services
Key Elements:
Clean and modern design that reflects the company's professional image and incorporates the company logo

Clear and easy-to-use navigation menu

“Homepage” that promotes the company's main services and includes the company's mission statement.

Services:

PROJECT MANAGEMENT
PROJECT ENGINEERING
QUALITY MANAGEMENT AND PROCESS DEVELOPMENT
BUSINESS CASE DEVELOPMENT
ENGINEERING & DESIGN MANAGEMENT
CONCEPT STUDIES AND PROJECT SUPPORT
CONSTRUCTION MANAGEMENT
CONTRACT MANAGEMENT / CLAIMS PROCUREMENT / SUPPLY CHAIN SUPPORT
COMMERCIAL LIABILITY & RISK MANAGEMENT

Mission Statement:

"Our mission at Travex is to provide expert project management and engineering consultancy services that help our clients achieve their goals and exceed their expectations. We will accomplish this by offering a full range of services, providing experienced and highly-qualified professionals, building strong relationships with our clients, continuously improving our services, and maintaining a reputation for excellence."

"About" page that includes client-supplied text about the company
"Contact" page with an editable form, email, and phone number for potential clients to get in touch with the company

Design Style:

Professional and modern
Clean and simple layout
Use of the company's colors and branding (subject to change)
Use of high-quality images that reflect the industry and services

Functionality:
Responsive design that is optimized for all devices and screen sizes

Website will be coded and uploaded to a content management system (CMS) for easy updates and maintenance
Website will be optimized for search engines and include all necessary SEO elements
Website will be fully tested for compatibility with all modern web browsers and devices
Website will be secured with an SSL certificate to ensure the safety of user data (client hosting includes SSL certificate).

Target Market(s)

Clients in the Oil & Gas, LNG, and Chemical industry Businesses and organizations in need of project management and engineering consultancy services Potential clients looking for information about the company and its services

Industry/Entity Type

Oil & Gas, LNG, and Chemical industry Businesses and organizations

Coding

Coded - Design and coding required

Number of Pages Required

3 page

Font styles to use
Sans Serif

Colors
0054AA
0677BA
7BADD7
CADEEF
E8F1F8
EB3D1F
EC4F4E
F09395
F8D3D4
FCEDEE
6B429C
8869AF
B7A5CE
E3DAEB
F3F0F8

Requirements
Must have
• HOME ABOUT AND CONTACT PAGE
Nice to have
• Fresh look, open to ideas
Should not have
• Stock images and hand shakes and meeting rooms..

```html
<!DOCTYPE html>
<html lang="en">
<head>
<meta charset="utf-8">
<title>Travex Resources</title>
<link rel="stylesheet" href="https://fonts.googleapis.com/css2?family=Montserrat:wght@400;500;600;700;800&display=swap">
<style>
:root{
  --blue:#2aa5f1;
  --blue-dark:#0677ba;
  --ink:#1f1f1f;
  --text:#222;
  --muted:#9a9a9a;
  --btn:#3a3a3a;
  --soft:#f6f6f6;
  --line:#dadada;
  --night:#15202c;
  --white:#fff;
}
*{box-sizing:border-box;margin:0;padding:0}
html,body{width:1200px;height:2758px;overflow:hidden;background:var(--white)}
body{position:relative;font-family:'Montserrat',sans-serif;color:var(--text)}
.abs{position:absolute}
a{text-decoration:none}
.brand{display:flex;flex-direction:column;align-items:center;width:206px}
.brand-mark{width:62px;height:62px;border-radius:50%;background:var(--blue);margin-bottom:12px}
.brand-name{font-weight:700;font-size:20px;color:var(--blue);letter-spacing:-.3px;white-space:nowrap}
.pill{display:inline-flex;align-items:center;justify-content:center;border-radius:20px;background:var(--btn);color:#fff;font-size:14px;font-weight:500}

/* social circles with invented network initials */
.socials{display:flex;gap:10px}
.social{width:24px;height:24px;border-radius:50%;display:flex;align-items:center;justify-content:center;font-size:11px;font-weight:700;line-height:1}
.topbar .social{background:transparent;color:#fff;border:1.5px solid rgba(255,255,255,.8)}
.topbar .social.on{background:var(--blue);border-color:var(--blue)}
.bottom-bar .social{background:#fff;color:var(--night)}
.bottom-bar .social.on{background:var(--blue);color:#fff;border:2px solid #fff}

/* hero */
.hero{left:0;top:0;width:1200px;height:560px;overflow:hidden;
  background:
    radial-gradient(ellipse 340px 220px at 170px 190px,rgba(200,205,210,.35),transparent 70%),
    radial-gradient(ellipse 420px 200px at 660px 380px,rgba(214,160,52,.75),transparent 70%),
    radial-gradient(ellipse 300px 260px at 1020px 200px,rgba(150,165,185,.35),transparent 70%),
    linear-gradient(180deg,#262a2f 0%,#3a3832 40%,#5e4d2b 70%,#3a3b3d 100%)}
.hero-photo{position:absolute;inset:0}
.hero .brand{left:125px;top:12px}
.topbar{left:762px;top:16px;display:flex;align-items:center;gap:10px;color:#fff;font-weight:600;font-size:14px;letter-spacing:.6px}
.topbar .ring{width:28px;height:28px;border-radius:50%;background:var(--blue-dark);display:flex;align-items:center;justify-content:center}
.topbar .sep{width:1px;height:30px;background:rgba(255,255,255,.35);margin:0 14px}
.nav{top:68px;left:664px;display:flex;gap:37px;font-weight:600;font-size:13px;color:#fff;letter-spacing:.4px}
.nav .active{color:var(--blue);text-decoration:underline}
.hero-title{left:0;top:250px;width:1200px;text-align:center;color:#fff;font-weight:800;font-size:40px;line-height:45px}
.hero .pill{left:545px;top:360px;width:135px;height:34px}
.slider-dots{left:576px;top:514px;display:flex;gap:11px}
.slider-dots span{width:13px;height:13px;border-radius:50%;border:2px solid #fff}
.slider-dots .on{background:var(--blue)}
.hero-wave{left:0;top:400px;width:1200px;height:200px}

/* services */
.section-title{font-weight:700;color:var(--blue);font-size:35px;letter-spacing:.5px}
.services-title{left:0;top:628px;width:1200px;text-align:center}
.card{position:absolute;width:257px;text-align:center}
.card .thumb{position:relative;height:182px;border:2px solid var(--blue);border-radius:5px;padding:3px;background:#fff}
.card .thumb .shot{width:100%;height:100%;border-radius:3px}
.card p{margin-top:10px;font-size:14px;font-weight:500;line-height:19px;color:var(--ink)}
.plus{position:absolute;left:50%;top:50%;width:64px;height:64px;margin:-32px 0 0 -32px;border-radius:50%;background:var(--blue);display:flex;align-items:center;justify-content:center}
.view-all{left:544px;top:1204px;width:112px;height:34px}

/* mission */
.mission{left:0;top:1311px;width:1200px;height:531px;background:var(--soft)}
.mission-block{left:126px;top:1493px;width:175px;height:274px;background:var(--blue)}
.mission-photo{left:145px;top:1387px;width:478px;height:362px;
  background:
    radial-gradient(ellipse 120px 150px at 80px 180px,rgba(240,180,40,.85),transparent 75%),
    radial-gradient(ellipse 110px 90px at 270px 90px,rgba(245,200,40,.9),transparent 70%),
    radial-gradient(ellipse 170px 170px at 290px 260px,rgba(40,60,120,.95),transparent 75%),
    radial-gradient(ellipse 120px 200px at 430px 160px,rgba(220,190,70,.6),transparent 75%),
    linear-gradient(135deg,#c9a24a 0%,#8c7a4f 40%,#3b4d7a 70%,#b9b2a0 100%)}
.mission-copy{left:690px;top:1415px;width:350px}
.mission-copy .section-title{font-size:33px}
.mission-copy p{margin-top:22px;font-size:12.3px;line-height:17.7px;color:var(--ink)}
.mission-copy p+p{margin-top:15px}
.about-btn{left:690px;top:1679px;width:174px;height:34px;background:var(--blue)}

/* inquiry */
.agent-block{left:899px;top:2058px;width:175px;height:299px;background:var(--blue)}
.agent-photo{left:499px;top:1916px;width:558px;height:424px;
  background:
    radial-gradient(ellipse 150px 200px at 370px 300px,rgba(150,170,205,.95),transparent 75%),
    radial-gradient(ellipse 90px 110px at 380px 150px,rgba(40,32,30,.85),transparent 70%),
    repeating-linear-gradient(90deg,rgba(255,255,255,.35) 0 22px,rgba(200,205,212,.2) 22px 60px),
    linear-gradient(90deg,#dfe3e6 0%,#cfd6dd 40%,#a9b6c7 70%,#e7ebef 100%)}
.form-card{left:126px;top:1973px;width:538px;height:368px;background:#fff;box-shadow:0 0 22px rgba(0,0,0,.07)}
.form-card .section-title{position:absolute;left:0;top:40px;width:100%;text-align:center;font-size:33px}
.field{position:absolute;border:1px solid var(--line);display:flex;align-items:center;gap:9px;padding-left:15px;font-size:12px;color:var(--muted);background:#fff}
.field.area{align-items:flex-start;padding-top:14px}
.submit{left:341px;top:2279px;width:108px;height:34px;font-size:15px}

/* footer */
.footer{left:0;top:2400px;width:1200px;height:358px;
  background:
    radial-gradient(ellipse 300px 140px at 250px 120px,rgba(90,80,50,.35),transparent 70%),
    radial-gradient(ellipse 300px 140px at 900px 90px,rgba(70,80,95,.35),transparent 70%),
    linear-gradient(180deg,#1b2836 0%,#0f1a26 100%)}
.footer-wave{left:0;top:2400px;width:1200px;height:120px}
.footer .brand{left:125px;top:140px}
.foot-col{position:absolute;color:#fff;font-size:12.5px}
.foot-col h4{color:var(--blue);font-size:17px;font-weight:700;margin-bottom:12px}
.info-row{display:flex;gap:12px;margin-bottom:13px;line-height:18px}
.info-row svg{flex:none;margin-top:2px}
.links a{display:block;color:#fff;margin-bottom:9px;font-size:12.5px}
.links a.current{color:var(--blue);text-decoration:underline}
.map{left:830px;top:131px;width:244px;height:141px;
  background:
    radial-gradient(ellipse 60px 40px at 60px 100px,rgba(170,200,150,.8),transparent 70%),
    radial-gradient(ellipse 70px 40px at 190px 110px,rgba(190,210,170,.8),transparent 70%),
    linear-gradient(135deg,#dfe8d6 0%,#ece4cc 50%,#cfdcc4 100%)}
.bottom-bar{left:0;top:2719px;width:1200px;height:39px;background:var(--blue);display:flex;align-items:center;justify-content:space-between;padding:0 126px;color:#fff;font-size:12px}
</style>
</head>
<body>

<header class="abs hero">
  <div class="hero-photo" role="img" aria-label="Oil and gas processing plant with pipework"></div>
  <div class="abs brand"><span class="brand-mark"></span><span class="brand-name">TRAVEX RESOURCES</span></div>
  <div class="abs topbar">
    <span class="ring"><svg width="14" height="14" viewBox="0 0 24 24"><path fill="#fff" d="M6.6 10.8a15 15 0 0 0 6.6 6.6l2.2-2.2a1 1 0 0 1 1-.25 11.4 11.4 0 0 0 3.6.57 1 1 0 0 1 1 1V20a1 1 0 0 1-1 1A17 17 0 0 1 3 4a1 1 0 0 1 1-1h3.5a1 1 0 0 1 1 1c0 1.25.2 2.45.57 3.57a1 1 0 0 1-.25 1z"/></svg></span>
    <span>+000-555-0142</span>
    <span class="sep"></span>
    <div class="socials">
      <span class="social" aria-label="Kiro">K</span><span class="social on" aria-label="Vela">V</span><span class="social" aria-label="Orbi">O</span><span class="social" aria-label="Luma">L</span>
    </div>
  </div>
  <nav class="abs nav"><span class="active">HOME</span><span>SERVICES</span><span>OUR MISSION</span><span>CONTACT US</span></nav>
  <h1 class="abs hero-title">VITAL OIL AND NATURAL<br>GAS RESOURCES</h1>
  <a class="abs pill">Contact Us</a>
  <svg class="abs hero-wave" viewBox="0 0 1200 200" preserveAspectRatio="none">
    <path fill="#2aa5f1" d="M0 30 C150 -5 280 10 420 60 C540 105 610 150 690 150 C820 148 960 40 1200 48 L1200 200 L0 200Z"/>
    <path fill="#fff" d="M0 52 C150 20 280 40 420 95 C540 140 600 158 660 156 C800 150 980 60 1200 102 L1200 200 L0 200Z"/>
  </svg>
</header>
<div class="abs slider-dots"><span></span><span class="on"></span><span></span></div>

<h2 class="abs section-title services-title">OUR SERVICES</h2>

<div class="card" style="left:186px;top:701px"><div class="thumb"><div class="shot" role="img" aria-label="Engineers reviewing project drawings" style="background:radial-gradient(ellipse 60px 40px at 50px 30px,rgba(240,170,40,.9),transparent 70%),radial-gradient(ellipse 120px 60px at 130px 130px,rgba(235,235,235,.95),transparent 70%),linear-gradient(135deg,#b9a57a,#8f9aa3 55%,#e5e2dc)"></div></div><p>Project Management</p></div>
<div class="card" style="left:472px;top:701px"><div class="thumb"><div class="shot" role="img" aria-label="Engineers inspecting a plant" style="background:radial-gradient(ellipse 50px 40px at 110px 60px,rgba(240,170,30,.9),transparent 70%),radial-gradient(ellipse 110px 70px at 100px 140px,rgba(40,50,70,.9),transparent 70%),linear-gradient(135deg,#9fb1c2,#6a7787 55%,#d8a93a)"></div></div><p>Project Engineering</p></div>
<div class="card" style="left:759px;top:701px"><div class="thumb"><div class="shot" role="img" aria-label="Quality management concept" style="background:radial-gradient(circle at 135px 90px,rgba(230,235,240,.55),transparent 35%),radial-gradient(ellipse 90px 40px at 120px 160px,rgba(30,30,35,.7),transparent 70%),linear-gradient(135deg,#7f8b98,#4a5460 55%,#a7b0b8)"></div></div><p>Quality Management &amp;<br>Process Development</p></div>
<div class="card" style="left:186px;top:946px"><div class="thumb"><div class="shot" role="img" aria-label="Business case study concept" style="background:radial-gradient(circle at 125px 80px,rgba(120,135,150,.45),transparent 40%),radial-gradient(ellipse 50px 40px at 215px 130px,rgba(200,160,140,.6),transparent 70%),linear-gradient(135deg,#1c2836,#0e151e 60%,#3b4754)"></div></div><p>Business Case Development</p></div>
<div class="card" style="left:472px;top:946px"><div class="thumb"><div class="shot" role="img" aria-label="Engineer working on a design screen" style="background:radial-gradient(ellipse 90px 60px at 80px 90px,rgba(140,150,160,.6),transparent 70%),radial-gradient(ellipse 50px 70px at 215px 80px,rgba(170,140,120,.5),transparent 70%),linear-gradient(135deg,#3b4654,#1e2630 60%,#4c5866)"></div><span class="plus"><svg width="30" height="30" viewBox="0 0 30 30"><path d="M15 2v26M2 15h26" stroke="#fff" stroke-width="3"/></svg></span></div><p>Engineering &amp; Design<br>Management</p></div>
<div class="card" style="left:759px;top:946px"><div class="thumb"><div class="shot" role="img" aria-label="Site worker at a gas facility" style="background:radial-gradient(ellipse 50px 35px at 80px 45px,rgba(245,200,30,.95),transparent 70%),radial-gradient(ellipse 70px 60px at 70px 140px,rgba(130,200,60,.8),transparent 70%),radial-gradient(ellipse 90px 70px at 190px 120px,rgba(220,200,60,.8),transparent 70%),linear-gradient(135deg,#b7c7d4,#d2b25a 50%,#7a8a52)"></div></div><p>Concept Studies and Project<br>Support</p></div>

<a class="abs pill view-all">View All</a>

<section class="abs mission"></section>
<div class="abs mission-block"></div>
<div class="abs mission-photo" role="img" aria-label="Smiling plant worker in hard hat"></div>
<div class="abs mission-copy">
  <h2 class="section-title">OUR MISSION</h2>
  <p>Our mission at Travex is to provide expert project management and engineering consultancy services that help our clients achieve their goals and exceed their expectations.</p>
  <p>We will accomplish this by offering a full range of services, providing experienced and highly-qualified professionals, building strong relationships with our clients, continuously improving our services, and maintaining a reputation for excellence.</p>
</div>
<a class="abs pill about-btn">About Company</a>

<div class="abs agent-block"></div>
<div class="abs agent-photo" role="img" aria-label="Support agent with headset at a desk"></div>
<div class="abs form-card">
  <h2 class="section-title">QUICK INQUIRY</h2>
</div>
<div class="field" style="left:158px;top:2073px;width:231px;height:35px"><svg width="13" height="13" viewBox="0 0 14 14" fill="none" stroke="#999"><circle cx="7" cy="4" r="3"/><path d="M1 13c0-3 3-5 6-5s6 2 6 5z"/></svg>First Name</div>
<div class="field" style="left:401px;top:2073px;width:230px;height:35px"><svg width="13" height="13" viewBox="0 0 14 14" fill="none" stroke="#999"><circle cx="7" cy="4" r="3"/><path d="M1 13c0-3 3-5 6-5s6 2 6 5z"/></svg>Last Name</div>
<div class="field" style="left:158px;top:2120px;width:231px;height:35px"><svg width="13" height="11" viewBox="0 0 14 11" fill="none" stroke="#999"><rect x=".5" y=".5" width="13" height="10"/><path d="M.5 .5l6.5 5 6.5-5"/></svg>Email</div>
<div class="field" style="left:401px;top:2120px;width:230px;height:35px"><svg width="10" height="13" viewBox="0 0 10 14" fill="none" stroke="#999"><rect x=".5" y=".5" width="9" height="13" rx="1"/></svg>Phone</div>
<div class="field area" style="left:158px;top:2168px;width:473px;height:72px"><svg width="12" height="12" viewBox="0 0 12 12" fill="none" stroke="#999"><path d="M.5 .5h11v7l-4 4h-7z"/></svg>How can we help?</div>
<a class="abs pill submit">Submit</a>

<footer class="abs footer">
  <div class="abs brand"><span class="brand-mark"></span><span class="brand-name">TRAVEX RESOURCES</span></div>
  <div class="foot-col" style="left:382px;top:133px;width:240px">
    <h4>Conatct info</h4>
    <div class="info-row"><svg width="14" height="17" viewBox="0 0 14 18"><path fill="#2aa5f1" d="M7 0a7 7 0 0 0-7 7c0 5 7 11 7 11s7-6 7-11a7 7 0 0 0-7-7zm0 10a3 3 0 1 1 0-6 3 3 0 0 1 0 6z"/></svg><span>lorem ipsum. 18, 6000 Harbour Lane, Perth</span></div>
    <div class="info-row"><svg width="14" height="14" viewBox="0 0 24 24"><path fill="#2aa5f1" d="M6.6 10.8a15 15 0 0 0 6.6 6.6l2.2-2.2a1 1 0 0 1 1-.25 11.4 11.4 0 0 0 3.6.57 1 1 0 0 1 1 1V20a1 1 0 0 1-1 1A17 17 0 0 1 3 4a1 1 0 0 1 1-1h3.5a1 1 0 0 1 1 1c0 1.25.2 2.45.57 3.57a1 1 0 0 1-.25 1z"/></svg><span>+000-555-0142</span></div>
    <div class="info-row" style="font-size:14px"><svg width="15" height="11" viewBox="0 0 15 11"><rect width="15" height="11" fill="#2aa5f1"/><path d="M0 0l7.5 6L15 0" stroke="#15202c" fill="none"/></svg><span>info@travexresources.com</span></div>
  </div>
  <div class="foot-col links" style="left:654px;top:133px">
    <h4>Quick Link</h4>
    <a class="current">Home</a><a>Services</a><a>Our Mission</a><a>Contact Us</a>
  </div>
  <div class="abs map" role="img" aria-label="Location map"></div>
</footer>
<svg class="abs footer-wave" viewBox="0 0 1200 120" preserveAspectRatio="none">
  <path fill="#2aa5f1" d="M0 86 C200 30 420 0 640 12 C860 24 1000 70 1200 70 L1200 100 C1000 100 860 60 640 54 C420 48 220 90 0 100Z"/>
  <path fill="#fff" d="M0 0 H1200 V62 C1000 62 860 14 640 14 C420 12 200 36 0 76Z"/>
</svg>
<div class="abs bottom-bar"><span>© 2023 Travex Resources. All Right Reserved</span>
  <div class="socials">
    <span class="social" aria-label="Kiro">K</span><span class="social on" aria-label="Vela">V</span><span class="social" aria-label="Orbi">O</span><span class="social" aria-label="Luma">L</span>
  </div>
</div>

</body>
</html>
```